Powerpoint design for european B2B business

We need a Powerpoint design for a newly established IT company with a B2B focus. We want to develop management information systems that help managers communicate goals into their organization and analyze their organizational activities and performance.

We defined the attached color scale, please relate your design to these colors.

The design should be simple and straight, serious and professional and leave enough space for the content ... :-)

Target Market(s)

B2B, companies larger than 200 employees

Industry/Entity Type

Business

Font styles to use
Sans Serif

Requirements
Should not have
• too playful design, clipart style

```html
<!DOCTYPE html>
<html lang="en">
<head>
<meta charset="utf-8">
<title>Velnora – Presentation Slide Set</title>
<link href="https://fonts.googleapis.com/css2?family=Open+Sans:wght@400;600;700&display=swap" rel="stylesheet">
<style>
  :root{
    --navy:#274a6e;
    --navy-deep:#1f3d5c;
    --green:#8dc19a;
    --red:#c8354c;
    --ink:#1d3550;
    --text:#8a96a3;
    --rule:#dfe4ea;
    --page:#ffffff;
    --stage:#ffffff;
  }
  *{box-sizing:border-box;margin:0;padding:0}
  html,body{width:1200px;height:1119px;overflow:hidden;background:var(--stage)}
  body{font-family:"Open Sans",Arial,sans-serif;position:relative}
  .sprites{position:absolute;width:0;height:0}
  .slide-grid{position:absolute;left:7px;top:6px;display:grid;
    grid-template-columns:repeat(3,387px);grid-template-rows:repeat(5,216.5px);
    column-gap:12px;row-gap:7.5px}
  .slide{position:relative;width:387px;height:216.5px;background:var(--page);overflow:hidden;
    box-shadow:0 0 0 .5px #e3e7ec}
  .slide.dark{background:var(--navy)}
  .abs{position:absolute}
  .photo{position:absolute}
  .footer{position:absolute;left:0;bottom:0;width:100%;height:8px;background:var(--navy);
    color:#fff;font-size:3.6px;line-height:8px;padding-left:6px}
  .footer .page-no{position:absolute;right:0;top:0;width:13px;height:8px;background:var(--green)}
  .footer .page-no span{position:absolute;right:16px;color:#fff}
  .brand{position:absolute;right:14px;top:12px;color:var(--navy);
    font-weight:400;font-size:14px;line-height:16px;letter-spacing:.2px;white-space:nowrap}
  .brand.light{color:#fff}
  .brand.big{font-size:24px;line-height:28px}
  .slide-title{position:absolute;left:16px;top:14px;color:var(--navy);font-size:15.5px;font-weight:400;line-height:18px}
  .slide-title::after{content:"";position:absolute;left:0;bottom:-5px;width:32px;height:1.2px;background:var(--green)}
  .slide-title.nobar::after{display:none}
  .lead{position:absolute;color:var(--ink);font-weight:700;font-size:7px;line-height:9.5px}
  .body{position:absolute;color:var(--text);font-size:4.5px;line-height:6.2px}
  .body p+p{margin-top:5px}
  .heading{color:var(--navy);font-size:6.5px;font-weight:600;line-height:8px}
  .col-rule{position:absolute;width:.6px;background:var(--rule)}
  .icon-row{position:absolute;display:flex;align-items:flex-start;gap:7px}
  .icon-row svg{flex:none}
  .icon-row .label{font-size:5.5px;line-height:7px;color:#fff}
  .icon-row .label small{display:block;font-size:4px;line-height:5px;opacity:.85}
  .icon-row.on-light .label{color:var(--navy)}
  .icon-row.on-light .label small{color:var(--text)}
  .ico{display:block}
  .num-box{position:absolute;left:192px;width:160px;height:27px;display:flex;align-items:center;color:#fff}
  .num-box .n{width:24px;text-align:center;font-size:15px;font-weight:600;border-right:1px solid rgba(255,255,255,.8);line-height:16px}
  .num-box .t{font-size:4.5px;line-height:6px;padding-left:7px;padding-right:6px}
  .svc{position:absolute;left:16px;display:flex;gap:8px}
  .svc .name{font-size:6.5px;line-height:8px}
  .svc .body{position:static}
  .center-col{position:absolute;text-align:center}
  .center-col .heading{font-size:5px}
  .center-col svg{margin:0 auto 4px}
</style>
</head>
<body>

<svg class="sprites" aria-hidden="true">
  <defs>
    <symbol id="i-search" viewBox="0 0 20 20"><circle cx="8.5" cy="8.5" r="5" fill="none" stroke="currentColor" stroke-width="2.2"/><path d="M12.2 12.2 17 17" stroke="currentColor" stroke-width="2.6" stroke-linecap="round"/></symbol>
    <symbol id="i-pen" viewBox="0 0 20 20"><path d="M4 16l1-4 8-8 3 3-8 8z" fill="currentColor"/><path d="M4 16l1-4 3 3z" fill="currentColor" opacity=".6"/></symbol>
    <symbol id="i-rocket" viewBox="0 0 20 20"><path d="M15.5 4.5c-4 0-7 3-8.5 6.5l2 2c3.5-1.5 6.5-4.5 6.5-8.5z" fill="currentColor"/><path d="M7 11 4 12l2-4h3zM9 13l-1 3 4-2v-3z" fill="currentColor"/><path d="M5.5 14.5 3.5 16.5" stroke="currentColor" stroke-width="1.6" stroke-linecap="round"/></symbol>
    <symbol id="i-gear" viewBox="0 0 20 20"><circle cx="10" cy="10" r="5.6" fill="none" stroke="currentColor" stroke-width="3.4" stroke-dasharray="2.4 1.6"/><circle cx="10" cy="10" r="4" fill="none" stroke="currentColor" stroke-width="2"/></symbol>
    <symbol id="i-bars" viewBox="0 0 20 20"><path d="M4 16V11M8 16V8M12 16V10M16 16V5" stroke="currentColor" stroke-width="2.4"/></symbol>
    <symbol id="i-cup" viewBox="0 0 20 20"><path d="M3 9h11v3a5 5 0 0 1-5 5H8a5 5 0 0 1-5-5z" fill="currentColor"/><path d="M14 10h1.5a2 2 0 0 1 0 4H14" fill="none" stroke="currentColor" stroke-width="1.4"/><path d="M7 3c-1 1.5 1 2-0 4M10 3c-1 1.5 1 2 0 4" fill="none" stroke="currentColor" stroke-width="1.1"/><path d="M2 18.5h15" stroke="currentColor" stroke-width="1.2"/></symbol>
    <symbol id="i-trophy" viewBox="0 0 20 20"><path d="M6 4h8v4a4 4 0 0 1-8 0zM10 12v3M7 16h6" fill="none" stroke="currentColor" stroke-width="1.5"/><path d="M6 5H3.5a2.5 2.5 0 0 0 2.5 3.5M14 5h2.5a2.5 2.5 0 0 1-2.5 3.5" fill="none" stroke="currentColor" stroke-width="1.2"/></symbol>
    <symbol id="i-crown" viewBox="0 0 20 20"><path d="M3.5 14.5 3 7l4 3 3-5 3 5 4-3-.5 7.5z" fill="none" stroke="currentColor" stroke-width="1.5" stroke-linejoin="round"/></symbol>
    <symbol id="i-badge" viewBox="0 0 20 20"><circle cx="10" cy="8.5" r="4.5" fill="none" stroke="currentColor" stroke-width="1.6"/><path d="M7.5 12.5 6.5 17l3.5-2 3.5 2-1-4.5" fill="none" stroke="currentColor" stroke-width="1.4"/></symbol>
    <symbol id="i-people" viewBox="0 0 20 20"><circle cx="7" cy="7" r="2.5" fill="currentColor"/><circle cx="13.5" cy="7" r="2.5" fill="currentColor"/><path d="M2.5 15a4.5 4 0 0 1 9 0zM9 15a4.5 4 0 0 1 9 0z" fill="currentColor"/></symbol>

    <symbol id="c-search" viewBox="0 0 20 20"><circle cx="10" cy="10" r="10" fill="var(--navy)"/><use href="#i-search" x="4" y="4" width="12" height="12" color="#fff"/></symbol>
    <symbol id="c-pen" viewBox="0 0 20 20"><circle cx="10" cy="10" r="10" fill="var(--navy)"/><use href="#i-pen" x="4" y="4" width="12" height="12" color="#fff"/></symbol>
    <symbol id="c-rocket" viewBox="0 0 20 20"><circle cx="10" cy="10" r="10" fill="var(--navy)"/><use href="#i-rocket" x="4" y="4" width="12" height="12" color="#fff"/></symbol>
    <symbol id="c-gear" viewBox="0 0 20 20"><circle cx="10" cy="10" r="10" fill="var(--navy)"/><use href="#i-gear" x="4" y="4" width="12" height="12" color="#fff"/></symbol>
    <symbol id="c-bars" viewBox="0 0 20 20"><circle cx="10" cy="10" r="10" fill="var(--navy)"/><use href="#i-bars" x="4" y="4" width="12" height="12" color="#fff"/></symbol>
    <symbol id="o-trophy" viewBox="0 0 20 20"><circle cx="10" cy="10" r="9.3" fill="none" stroke="var(--navy)" stroke-width="1"/><use href="#i-trophy" x="4.5" y="4.5" width="11" height="11" color="var(--navy)"/></symbol>
    <symbol id="o-crown" viewBox="0 0 20 20"><circle cx="10" cy="10" r="9.3" fill="none" stroke="var(--navy)" stroke-width="1"/><use href="#i-crown" x="4.5" y="4.5" width="11" height="11" color="var(--navy)"/></symbol>
    <symbol id="o-rocket" viewBox="0 0 20 20"><circle cx="10" cy="10" r="9.3" fill="none" stroke="var(--navy)" stroke-width="1"/><use href="#i-rocket" x="4.5" y="4.5" width="11" height="11" color="var(--navy)"/></symbol>
  </defs>
</svg>

<main class="slide-grid">

  <!-- 1: cover with feature list -->
  <section class="slide">
    <div class="photo" role="img" aria-label="Photo of a glass office tower seen from below" style="left:0;top:0;width:193px;height:216.5px;background:linear-gradient(160deg,#dbe6ef 0%,#a7bccd 35%,#6b879f 70%,#3d5872 100%)"></div>
    <div class="abs" style="left:193px;top:0;width:194px;height:216.5px;background:var(--navy)"></div>
    <div class="brand light" style="top:20px">Velnora</div>
    <div class="icon-row" style="left:218px;top:62px"><svg class="ico" width="12" height="12" color="#fff"><use href="#i-search"/></svg><div class="label">Your Text Here<small>Lorem ipsum dolor sit amet, consectetur adipiscing elit,<br>sed do eiusmod.</small></div></div>
    <div class="icon-row" style="left:218px;top:93px"><svg class="ico" width="12" height="12" color="#fff"><use href="#i-pen"/></svg><div class="label">Your Text Here<small>Lorem ipsum dolor sit amet, consectetur adipiscing elit,<br>sed do eiusmod.</small></div></div>
    <div class="icon-row" style="left:218px;top:124px"><svg class="ico" width="12" height="12" color="#fff"><use href="#i-rocket"/></svg><div class="label">Your Text Here<small>Lorem ipsum dolor sit amet, consectetur adipiscing elit,<br>sed do eiusmod.</small></div></div>
    <div class="icon-row" style="left:218px;top:155px"><svg class="ico" width="12" height="12" color="#fff"><use href="#i-gear"/></svg><div class="label">Your Text Here<small>Lorem ipsum dolor sit amet, consectetur adipiscing elit,<br>sed do eiusmod.</small></div></div>
  </section>

  <!-- 2: title with photo collage -->
  <section class="slide">
    <div class="photo" role="img" aria-label="Navy toned photo behind the company name" style="left:5px;top:5px;width:118px;height:92px;background:radial-gradient(circle at 50% 50%,#4e6f92 0%,#2c4d70 60%,#223f5e 100%)"></div>
    <div class="brand light" style="left:5px;right:auto;top:43px;width:118px;text-align:center">Velnora</div>
    <div class="photo" role="img" aria-label="Photo of two businessmen in suits reviewing documents" style="left:5px;top:103px;width:118px;height:91px;background:linear-gradient(135deg,#dfe3e6 0%,#9ea6ad 50%,#3c4248 100%)"></div>
    <div class="photo" role="img" aria-label="Photo of a businessman talking on a mobile phone" style="left:129px;top:5px;width:126px;height:189px;background:linear-gradient(160deg,#c9ced2 0%,#a8adb2 40%,#4a4f55 75%,#24282c 100%)"></div>
    <div class="brand">Velnora</div>
    <div class="slide-title nobar" style="left:268px;top:38px;font-size:14.5px;line-height:16px">Your Title<br>Goes Here</div>
    <div class="body" style="left:268px;top:86px;width:102px"><p>Lorem ipsum dolor sit amet, consectetur adipiscing elit, sed do eiusmod tempor incididunt ut labore et commodo consequat dolore magna aliqua.</p><p>Duis aute irure dolor in reprehenderit in voluptate velit esse cillum dolore eu fugiat nulla pariatur.</p><p>Ut enim ad minim veniam, quis nostrud exercitation ullamco laboris nisi ut ex ea commodo consequat.</p></div>
    <div class="footer">© 2017 Velnora. All rights reserved.<div class="page-no"><span>14</span></div></div>
  </section>

  <!-- 3: header text with team photos -->
  <section class="slide">
    <div class="slide-title">Your Title Goes Here</div>
    <div class="brand">Velnora</div>
    <div class="lead" style="left:32px;top:70px;width:140px">This is place for your header<br>text. Insert your text here.</div>
    <div class="body" style="left:32px;top:92px;width:140px"><p>Lorem ipsum dolor sit amet, consectetur adipiscing elit, sed do eiusmod tempor incididunt ut labore et dolore magna aliqua. Ut enimad minim veniam, quis nostrud exercitation.</p><p>Excepteur sint occaecat cupidatat non proident, sunt inculpa qui officia deserunt mollit anim id est laborum.</p></div>
    <div class="photo" role="img" aria-label="Photo of a smiling businesswoman" style="left:194px;top:66px;width:58px;height:122px;background:linear-gradient(180deg,#eef2f5 0%,#e2d6cc 45%,#d7a8b2 75%,#c3cbd4 100%)"></div>
    <div class="photo" role="img" aria-label="Photo of a young businessman with a tablet" style="left:257px;top:66px;width:58px;height:122px;background:linear-gradient(180deg,#eef2f5 0%,#dcc8b8 40%,#9bb7d3 70%,#c4cfd9 100%)"></div>
    <div class="photo" role="img" aria-label="Photo of a businessman holding a tablet" style="left:320px;top:66px;width:58px;height:122px;background:linear-gradient(180deg,#eef2f5 0%,#8a6b55 40%,#e9eef2 70%,#c4cfd9 100%)"></div>
    <div class="footer">© 2017 Velnora. All rights reserved.<div class="page-no"><span>15</span></div></div>
  </section>

  <!-- 4: two column description -->
  <section class="slide">
    <div class="slide-title">Two Column Description</div>
    <div class="brand">Velnora</div>
    <div class="lead" style="left:18px;top:66px;width:320px">This is place for your header text. Insert your text here, just replace this text with your own text</div>
    <div class="body" style="left:18px;top:98px;width:162px"><p>Lorem ipsum dolor sit amet, consectetur adipiscing elit, sed do eiusmod tempor incididunt ut labore et dolore magna aliqua. Ut enimad minim veniam, quis nostrud exercitation ullamco laboris nisi ut aliquip ex ea commodo consequat.</p><p>Duis aute irure dolor in reprehenderit in voluptate velit esse cillum dolore eu fugiat nulla pariatur. Excepteur sint occaecat cupidatat non proident, sunt inculpa qui officia deserunt mollit anim id est laborum.</p></div>
    <div class="col-rule" style="left:189px;top:100px;height:56px"></div>
    <div class="body" style="left:198px;top:98px;width:162px"><p>Lorem ipsum dolor sit amet, consectetur adipiscing elit, sed do eiusmod tempor incididunt ut labore et dolore magna aliqua. Ut enimad minim veniam, quis nostrud exercitation ullamco laboris nisi ut aliquip ex ea commodo consequat.</p><p>Duis aute irure dolor in reprehenderit in voluptate velit esse cillum dolore eu fugiat nulla pariatur. Excepteur sint occaecat cupidatat non proident, sunt inculpa qui officia deserunt mollit anim id est laborum.</p></div>
    <div class="footer">© 2017 Velnora. All rights reserved.<div class="page-no"><span>16</span></div></div>
  </section>

  <!-- 5: coffee break -->
  <section class="slide dark">
    <div class="photo" role="img" aria-label="Dim navy toned photo of a coffee cup on a table" style="left:0;top:0;width:387px;height:216.5px;background:linear-gradient(180deg,#2b4a6b 0%,#27455f 55%,#213a52 78%,#1d334a 100%)"></div>
    <div class="brand light" style="top:18px">Velnora</div>
    <svg class="abs" style="left:75px;top:70px" width="20" height="20" color="#fff"><use href="#i-cup"/></svg>
    <div class="abs" style="left:40px;top:93px;width:90px;text-align:center;color:#fff;font-size:10px;font-weight:600;line-height:12px">COFFEE BREAK</div>
    <div class="abs" style="left:40px;top:107px;width:90px;text-align:center;color:#d6e0ea;font-size:5px">Back in 15 minutes</div>
  </section>

  <!-- 6: three column description -->
  <section class="slide">
    <div class="slide-title">Three Column Description</div>
    <div class="brand">Velnora</div>
    <div class="lead" style="left:26px;top:64px;width:320px">This is place for your header text. Insert your text here, just replace this text with your own text</div>
    <div class="body" style="left:26px;top:90px;width:100px"><p>Lorem ipsum dolor sit amet, consectetur adipiscing elit, sed do eiusmod tempor incididunt ut labore et dolore magna aliqua. Ut enimad minim veniam, quis nostrud exercitation ullamco laboris nisi ut aliquip ex ea commodo consequat.</p><p>Duis aute irure dolor in reprehenderit in voluptate velit esse cillum dolore eu fugiat nulla pariatur excepteur occaecat.</p></div>
    <div class="col-rule" style="left:130px;top:92px;height:86px"></div>
    <div class="body" style="left:137px;top:90px;width:100px"><p>Lorem ipsum dolor sit amet, consectetur adipiscing elit, sed do eiusmod tempor incididunt ut labore et dolore magna aliqua. Ut enimad minim veniam, quis nostrud exercitation ullamco laboris nisi ut aliquip ex ea commodo consequat.</p><p>Duis aute irure dolor in reprehenderit in voluptate velit esse cillum dolore eu fugiat nulla pariatur excepteur occaecat.</p></div>
    <div class="col-rule" style="left:244px;top:92px;height:86px"></div>
    <div class="body" style="left:252px;top:90px;width:100px"><p>Lorem ipsum dolor sit amet, consectetur adipiscing elit, sed do eiusmod tempor incididunt ut labore et dolore magna aliqua. Ut enimad minim veniam, quis nostrud exercitation ullamco laboris nisi ut aliquip ex ea commodo consequat.</p><p>Duis aute irure dolor in reprehenderit in voluptate velit esse cillum dolore eu fugiat nulla pariatur excepteur occaecat.</p></div>
    <div class="footer">© 2017 Velnora. All rights reserved.<div class="page-no"><span>18</span></div></div>
  </section>

  <!-- 7: photo with overlay panel -->
  <section class="slide">
    <div class="photo" role="img" aria-label="Photo of a steel and glass roof structure" style="left:0;top:0;width:387px;height:216.5px;background:linear-gradient(135deg,#eef1f4 0%,#a9b3bd 30%,#5f6b78 60%,#c7ced6 100%)"></div>
    <div class="abs" style="left:217px;top:0;width:150px;height:216.5px;background:rgba(39,74,110,.88)"></div>
    <div class="abs" style="left:217px;top:188px;width:150px;height:16px;background:var(--green);color:#fff;font-size:4.5px;text-align:center;line-height:16px">www.yourwebsite.com</div>
    <div class="brand light" style="right:28px;top:20px">Velnora</div>
    <svg class="abs" style="left:236px;top:66px" width="18" height="18"><circle cx="9" cy="9" r="8.5" fill="none" stroke="#fff" stroke-width=".8"/><use href="#i-rocket" x="4" y="4" width="10" height="10" color="#fff"/></svg>
    <svg class="abs" style="left:269px;top:66px" width="18" height="18"><circle cx="9" cy="9" r="8.5" fill="none" stroke="#fff" stroke-width=".8"/><use href="#i-badge" x="4" y="4" width="10" height="10" color="#fff"/></svg>
    <svg class="abs" style="left:302px;top:66px" width="18" height="18"><circle cx="9" cy="9" r="8.5" fill="none" stroke="#fff" stroke-width=".8"/><use href="#i-crown" x="4" y="4" width="10" height="10" color="#fff"/></svg>
    <div class="abs" style="left:225px;top:117px;width:134px;text-align:center;color:#fff;font-size:10.5px;line-height:13px">Your Title Goes Here</div>
    <div class="abs" style="left:228px;top:133px;width:128px;text-align:center;color:#e6edf3;font-size:4.8px;line-height:6.5px">Lorem ipsum dolor sit amet, consectetur adipiscing elit, sed do eiusmod tempor incididunt ut labore et dolore magna aliqua.</div>
  </section>

  <!-- 8: services -->
  <section class="slide">
    <div class="slide-title">Your Title Goes Here</div>
    <div class="brand">Velnora</div>
    <div class="heading abs" style="left:16px;top:45px">Heading Goes Here</div>
    <div class="body" style="left:16px;top:54px;width:355px">Lorem ipsum dolor sit amet, consectetur adipiscing elit, sed do eiusmod tempor incididunt ut labore et dolore magna aliqua. Ut enim minim veniam, quis nostrud exercitation ullamco laboris nisi ut aliquip ex ea commodo consequat.</div>
    <div class="svc" style="top:76px"><svg width="14" height="14"><circle cx="7" cy="7" r="7" fill="var(--navy)"/><use href="#i-bars" x="3.5" y="3.5" width="7" height="7" color="#fff"/></svg><div><div class="name" style="color:var(--navy)">Service Number One</div><div class="body" style="width:140px">Lorem ipsum dolor sit amet, consectetur adipiscing elit, sed do eiusmod tempor incididunt ut labore et dolore magna aliqua.</div></div></div>
    <div class="svc" style="top:111px"><svg width="14" height="14"><circle cx="7" cy="7" r="7" fill="var(--green)"/><use href="#i-rocket" x="3.5" y="3.5" width="7" height="7" color="#fff"/></svg><div><div class="name" style="color:var(--green)">Service Number Two</div><div class="body" style="width:140px">Lorem ipsum dolor sit amet, consectetur adipiscing elit, sed do eiusmod tempor incididunt ut labore et dolore magna aliqua.</div></div></div>
    <div class="svc" style="top:145px"><svg width="14" height="14"><circle cx="7" cy="7" r="7" fill="var(--red)"/><use href="#i-search" x="3.5" y="3.5" width="7" height="7" color="#fff"/></svg><div><div class="name" style="color:var(--red)">Service Number Three</div><div class="body" style="width:140px">Lorem ipsum dolor sit amet, consectetur adipiscing elit, sed do eiusmod tempor incididunt ut labore et dolore magna aliqua.</div></div></div>
    <div class="num-box" style="top:86px;background:var(--navy)"><div class="n">1</div><div class="t">Lorem ipsum dolor sit amet, consectetur adipiscing elit, sed do eiusmod tempor incididunt ut labore et dolore magna aliqua.</div></div>
    <div class="num-box" style="top:117px;background:var(--green)"><div class="n">2</div><div class="t">Lorem ipsum dolor sit amet, consectetur adipiscing elit, sed do eiusmod tempor incididunt ut labore et dolore magna aliqua.</div></div>
    <div class="num-box" style="top:148px;background:var(--red)"><div class="n">3</div><div class="t">Lorem ipsum dolor sit amet, consectetur adipiscing elit, sed do eiusmod tempor incididunt ut labore et dolore magna aliqua.</div></div>
    <div class="footer">© 2017 Velnora. All rights reserved.<div class="page-no"><span>20</span></div></div>
  </section>

  <!-- 9: title with photo grid -->
  <section class="slide">
    <div class="slide-title nobar" style="top:36px;font-size:14.5px;line-height:16px">Your Title<br>Goes Here</div>
    <div class="body" style="left:16px;top:77px;width:86px"><p>Lorem ipsum dolor sit amet, consectetur adipiscing elit, sed do eiusmod tempor incididunt ut labore et commodo consequat dolore magna aliqua.</p><p>Duis aute irure dolor in reprehenderit in voluptate velit esse cillum dolore eu fugiat nulla pariatur.</p><p>Ut enim ad minim veniam, quis nostrud exercitation ullamco.</p></div>
    <div class="photo" role="img" aria-label="Photo of hands working on a tablet at a desk" style="left:112px;top:5px;width:126px;height:184px;background:linear-gradient(150deg,#e8edf2 0%,#b6c3cf 40%,#57687a 70%,#2f3c4a 100%)"></div>
    <div class="photo" role="img" aria-label="Photo of a hand touching a tablet screen" style="left:243px;top:5px;width:118px;height:89px;background:linear-gradient(135deg,#dfe6ec 0%,#9fb0c0 55%,#5e7185 100%)"></div>
    <div class="photo" role="img" aria-label="Photo of printed charts on a desk" style="left:243px;top:99px;width:118px;height:90px;background:linear-gradient(135deg,#eef2f5 0%,#b9c7d4 50%,#6f8398 100%)"></div>
    <div class="footer">© 2017 Velnora. All rights reserved.<div class="page-no"><span>21</span></div></div>
  </section>

  <!-- 10: title, photo and icon list -->
  <section class="slide">
    <div class="slide-title" style="top:17px">Your Title</div>
    <div class="heading abs" style="left:16px;top:62px">Heading Goes Here</div>
    <div class="body" style="left:16px;top:72px;width:96px"><p>Lorem ipsum dolor sit amet, consectetur adipiscing elit, sed do eiusmod tempor incididunt ut labore et commodo consequat dolore magna aliqua.</p><p>Duis aute irure dolor in reprehenderit in voluptate velit esse cillum dolore eu fugiat nulla pariatur.</p><p>Ut enim ad minim veniam, quis nostrud exercitation ullamco laboris nisi ut aliquip ex ea commodo consequat.</p></div>
    <div class="photo" role="img" aria-label="Photo of two colleagues reviewing charts in an office" style="left:117px;top:0;width:132px;height:208.5px;background:linear-gradient(170deg,#f1f3f5 0%,#d6dbe0 35%,#7f8891 60%,#bfc8d8 85%,#9aa9c6 100%)"></div>
    <div class="brand">Velnora</div>
    <div class="icon-row on-light" style="left:262px;top:62px"><svg width="14" height="14"><use href="#c-search"/></svg><div class="label">Your Text Here<small>Lorem ipsum dolor sit amet, adipiscing<br>elit, sed do eiusmod.</small></div></div>
    <div class="icon-row on-light" style="left:262px;top:92px"><svg width="14" height="14"><use href="#c-pen"/></svg><div class="label">Your Text Here<small>Lorem ipsum dolor sit amet, adipiscing<br>elit, sed do eiusmod.</small></div></div>
    <div class="icon-row on-light" style="left:262px;top:122px"><svg width="14" height="14"><use href="#c-rocket"/></svg><div class="label">Your Text Here<small>Lorem ipsum dolor sit amet, adipiscing<br>elit, sed do eiusmod.</small></div></div>
    <div class="icon-row on-light" style="left:262px;top:152px"><svg width="14" height="14"><use href="#c-gear"/></svg><div class="label">Your Text Here<small>Lorem ipsum dolor sit amet, adipiscing<br>elit, sed do eiusmod.</small></div></div>
    <div class="footer">© 2017 Velnora. All rights reserved.<div class="page-no"><span>22</span></div></div>
  </section>

  <!-- 11: pictures with bullets -->
  <section class="slide">
    <div class="slide-title">Pictures with Bullets</div>
    <div class="brand">Velnora</div>
    <div class="photo" role="img" aria-label="Strip of four office photos: handshake, charts, glasses on reports, meeting room" style="left:50px;top:65px;width:270px;height:40px;background:linear-gradient(90deg,#cfd9e3 0%,#8fa6bd 25%,#e4eaf0 40%,#9fb3c8 60%,#d8e1ea 78%,#7e97b1 100%)"></div>
    <svg class="abs" style="left:106px;top:79px" width="13" height="13"><use href="#c-search"/></svg>
    <svg class="abs" style="left:172px;top:79px" width="13" height="13"><use href="#c-gear"/></svg>
    <svg class="abs" style="left:238px;top:79px" width="13" height="13"><circle cx="6.5" cy="6.5" r="6.5" fill="var(--navy)"/><use href="#i-people" x="2.5" y="2.5" width="8" height="8" color="#fff"/></svg>
    <div class="heading abs" style="left:50px;top:123px">Heading Goes Here</div>
    <div class="body" style="left:50px;top:132px;width:125px"><p>Lorem ipsum dolor sit amet, consectetur adipiscing elit, sed do eiusmod tempor incididunt ut labore et commodo consequat dolore magna aliqua.</p><p>Duis aute irure dolor in reprehenderit in voluptate velit cillum dolore eu fugiat nulla pariatur.</p></div>
    <div class="heading abs" style="left:203px;top:123px">Heading Goes Here</div>
    <div class="body" style="left:203px;top:132px;width:125px"><p>Lorem ipsum dolor sit amet, consectetur adipiscing elit, sed do eiusmod tempor incididunt ut labore et commodo consequat dolore magna aliqua.</p><p>Duis aute irure dolor in reprehenderit in voluptate velit cillum dolore eu fugiat nulla pariatur.</p></div>
    <div class="footer">© 2017 Velnora. All rights reserved.<div class="page-no"><span>23</span></div></div>
  </section>

  <!-- 12: divider -->
  <section class="slide dark">
    <div class="photo" role="img" aria-label="Navy toned photo of a glass hall interior" style="left:0;top:0;width:387px;height:216.5px;background:linear-gradient(135deg,#315476 0%,#2a4b6d 45%,#23415f 100%)"></div>
    <div class="brand light big" style="right:40px;top:36px">Velnora</div>
    <div class="abs" style="left:0;top:104px;width:387px;text-align:center;color:#fff;font-size:5px">Divider Page</div>
    <div class="abs" style="left:0;top:114px;width:387px;text-align:center;color:#fff;font-size:13.5px;line-height:16px">Your Title Goes Here</div>
    <div class="abs" style="left:0;top:132px;width:387px;text-align:center;color:#dfe7ef;font-size:7px">Your Subtitle Here</div>
  </section>

  <!-- 13: paragraph with three bullets -->
  <section class="slide">
    <div class="slide-title">Paragraph with Three Bullet</div>
    <div class="brand">Velnora</div>
    <div class="lead" style="left:18px;top:65px;width:320px">This is place for your header text. Insert your text here, just replace this text with your own text</div>
    <div class="body" style="left:18px;top:92px;width:104px"><p>Lorem ipsum dolor sit amet, consectetur adipiscing elit, sed do eiusmod tempor incididunt ut labore et dolore magna aliqua. Ut enimad minim veniam, quis nostrud exercitation ullamco laboris nisi ut aliquip ex ea commodo consequat.</p><p>Duis aute irure dolor in reprehenderit in voluptate velit esse cillum dolore eu fugiat nulla pariatur excepteur occaecat.</p></div>
    <div class="col-rule" style="left:130px;top:92px;height:90px"></div>
    <div class="center-col" style="left:146px;top:88px;width:68px"><svg width="16" height="16" style="display:block"><use href="#o-trophy"/></svg><div class="heading">Your Text Here</div><div class="body" style="position:static"><p>Lorem ipsum dolor sit amet, consectetur adipiscing elit, sed do eiusmod tempor incididunt ut labore et dolore.</p><p>Ut enimad minim veniam, quis nostrud exercitation ullamco laboris nisi ut commodo consequat.</p></div></div>
    <div class="center-col" style="left:219px;top:88px;width:68px"><svg width="16" height="16" style="display:block"><use href="#o-crown"/></svg><div class="heading">Your Text Here</div><div class="body" style="position:static"><p>Lorem ipsum dolor sit amet, consectetur adipiscing elit, sed do eiusmod tempor incididunt ut labore et aliqua.</p><p>Ut enimad minim veniam, quis nostrud exercitation ullamco laboris nisi ut commodo consequat.</p></div></div>
    <div class="center-col" style="left:292px;top:88px;width:68px"><svg width="16" height="16" style="display:block"><use href="#o-rocket"/></svg><div class="heading">Your Text Here</div><div class="body" style="position:static"><p>Lorem ipsum dolor sit amet, consectetur adipiscing elit, sed do eiusmod tempor incididunt ut labore et dolore.</p><p>Ut enimad minim veniam, quis nostrud exercitation ullamco laboris nisi ut commodo consequat.</p></div></div>
    <div class="footer">© 2017 Velnora. All rights reserved.<div class="page-no"><span>25</span></div></div>
  </section>

  <!-- 14: global experience -->
  <section class="slide">
    <div class="slide-title">Global Experience</div>
    <div class="brand">Velnora</div>
    <div class="photo" role="img" aria-label="Grey world map with navy dots marking office locations" style="left:88px;top:40px;width:256px;height:150px;background:#e1e4e7"></div>
    <svg class="abs" style="left:16px;top:154px" width="10" height="10"><circle cx="5" cy="5" r="5" fill="var(--navy)"/></svg>
    <div class="heading abs" style="left:30px;top:155px">Heading Goes Here</div>
    <div class="body" style="left:16px;top:167px;width:68px">Lorem ipsum dolor sit amet, consectetur adipiscing elit, sed do eiusmod tempor incididunt ut labore.</div>
    <div class="footer">© 2017 Velnora. All rights reserved.<div class="page-no"><span>26</span></div></div>
  </section>

  <!-- 15: multiple column area -->
  <section class="slide">
    <div class="slide-title">Multiple Column Area</div>
    <div class="brand">Velnora</div>
    <div class="center-col" style="left:16px;top:56px;width:62px"><svg width="14" height="14" style="display:block"><use href="#c-gear"/></svg><div class="heading">Your Text Here</div><div class="body" style="position:static">Lorem ipsum consectetur adipiscing elit.</div></div>
    <div class="center-col" style="left:83px;top:56px;width:62px"><svg width="14" height="14" style="display:block"><use href="#c-rocket"/></svg><div class="heading">Your Text Here</div><div class="body" style="position:static">Lorem ipsum consectetur adipiscing elit.</div></div>
    <div class="center-col" style="left:150px;top:56px;width:62px"><svg width="14" height="14" style="display:block"><use href="#c-search"/></svg><div class="heading">Your Text Here</div><div class="body" style="position:static">Lorem ipsum consectetur adipiscing elit.</div></div>
    <div class="center-col" style="left:217px;top:56px;width:62px"><svg width="14" height="14" style="display:block"><use href="#c-pen"/></svg><div class="heading">Your Text Here</div><div class="body" style="position:static">Lorem ipsum consectetur adipiscing elit.</div></div>
    <div class="center-col" style="left:284px;top:56px;width:62px"><svg width="14" height="14" style="display:block"><use href="#c-bars"/></svg><div class="heading">Your Text Here</div><div class="body" style="position:static">Lorem ipsum consectetur adipiscing elit.</div></div>
    <div class="abs" style="left:26px;top:111px;width:320px;height:.6px;background:var(--rule)"></div>
    <div class="heading abs" style="left:26px;top:124px">Heading Goes Here</div>
    <div class="body" style="left:26px;top:133px;width:150px"><p>Lorem ipsum dolor sit amet, consectetur adipiscing elit, sed do eiusmod tempor incididunt ut labore et commodo consequat dolore magna aliqua.</p><p>Duis aute irure dolor in reprehenderit in voluptate velit cillum dolore eu fugiat nulla pariatur.</p></div>
    <div class="heading abs" style="left:198px;top:124px">Heading Goes Here</div>
    <div class="body" style="left:198px;top:133px;width:150px"><p>Lorem ipsum dolor sit amet, consectetur adipiscing elit, sed do eiusmod tempor incididunt ut labore et commodo consequat dolore magna aliqua.</p><p>Duis aute irure dolor in reprehenderit in voluptate velit cillum dolore eu fugiat nulla pariatur.</p></div>
    <div class="footer">© 2017 Velnora. All rights reserved.<div class="page-no"><span>27</span></div></div>
  </section>

</main>
</body>
</html>
```